New Modern floristry business design

Hi, we are a new business based in Sydney called "velvet moss floristry"

With so many floristry's we need a good design that will set a great first impression.

A few descriptive words on how we envision velvet moss floristry:

-dynamic design
-minimal colour (colour can be used to enhance the design)
-black white grey (can include gold,silver,metallic shadowing)
Strong "VELVET MOSS" with a classy "FLORISTRY"
Bold with a touch of feminine

Industry/Entity Type

Business

Contact Information for Business Card

Velvet Moss Floristry,
Delphine Ruvek,
Velvetmossfloristry@quillmail.com.au

```html
<!DOCTYPE html>
<html lang="en">
<head>
<meta charset="utf-8">
<title>Velvet Moss Floristry – Business Cards</title>
<link href="https://fonts.googleapis.com/css2?family=EB+Garamond:wght@400&family=Tinos:wght@400;700&display=swap" rel="stylesheet">
<style>
  :root {
    --backdrop: #8a8a8a;
    --card-black: #000000;
    --card-charcoal: #1c1c1c;
    --strip-light: #ffffff;
    --strip-mid: #c9c9c9;
    --ink-white: #ffffff;
  }
  html, body {
    margin: 0;
    padding: 0;
    width: 1200px;
    height: 1000px;
    overflow: hidden;
    background: var(--backdrop);
  }
  .canvas {
    position: relative;
    width: 1200px;
    height: 1000px;
  }
  .card {
    position: absolute;
    width: 760px;
    height: 455px;
    border-radius: 18px;
    overflow: hidden;
    background: var(--card-black);
  }
  .card--front { left: 70px; top: 35px; }
  .card--back {
    left: 325px;
    top: 515px;
    background: radial-gradient(ellipse 45% 55% at 62% 45%, var(--card-charcoal) 0%, var(--card-black) 100%);
  }
  .floral-strip {
    position: absolute;
    left: 0;
    top: 0;
    width: 200px;
    height: 100%;
    background: linear-gradient(90deg, var(--strip-light) 0%, var(--strip-mid) 45%, #5a5a5a 78%, var(--card-black) 100%);
  }
  .wordmark {
    position: absolute;
    color: var(--ink-white);
    font-family: "EB Garamond", "Times New Roman", serif;
    font-weight: 400;
    text-align: center;
    line-height: 1;
  }
  .card--front .wordmark { left: 200px; width: 520px; top: 150px; }
  .card--front .wordmark__name { font-size: 78px; }
  .card--front .wordmark__trade { font-size: 64px; margin-top: 6px; }
  .card--back .wordmark { left: 195px; width: 560px; top: 45px; }
  .card--back .wordmark__name { font-size: 62px; }
  .card--back .wordmark__trade { font-size: 50px; margin-top: 4px; }
  .contact {
    position: absolute;
    left: 195px;
    width: 560px;
    top: 358px;
    text-align: center;
    color: var(--ink-white);
    font-family: "Tinos", "Times New Roman", serif;
    line-height: 1.05;
  }
  .contact__name { font-size: 36px; font-weight: 700; letter-spacing: 1px; }
  .contact__email { font-size: 24px; }
</style>
</head>
<body>
<main class="canvas">
  <section class="card card--front" aria-label="Business card front">
    <div class="floral-strip" role="img" aria-label="Black and white climbing flower and vine pattern fading into the card"></div>
    <div class="wordmark">
      <div class="wordmark__name">VelvetMoss</div>
      <div class="wordmark__trade">Floristry</div>
    </div>
  </section>

  <section class="card card--back" aria-label="Business card back">
    <div class="floral-strip" role="img" aria-label="Black and white climbing flower and vine pattern fading into the card"></div>
    <div class="wordmark">
      <div class="wordmark__name">VelvetMoss</div>
      <div class="wordmark__trade">Floristry</div>
    </div>
    <div class="contact">
      <div class="contact__name">DELPHINE RUVEK</div>
      <div class="contact__email">Velvetmossfloristry@quillmail.com.au</div>
    </div>
  </section>
</main>
</body>
</html>
```